Business Cards and Stationery - Real Estate
See "information" and "additional comments"
Business Cards and Stationery - Real Estate - Real Estate
Creative Brief
Professional
Anselm Varga
Managing Broker
4382 SW Route 14, Ste 305 Vancouver, WA 98671
Direct - 360-555-0147
Cell - 360-555-0193
anselm@fernloftpm.example
www.fernlofthomes.example
Licensed in ID & MT
We want to use UV spotting on our cards. Here is a video link from the printing company we are using. If you are unfamiliar with creating files for UV spotting, it requires one file for the card and a second mask file for the UV spotting. https://www.clipvault.example/watch?v=Qx7rLm2PzA1 I've uploaded the template files to use from Zentra Print along with our Adobe Illustrator Logo files and a head shot. We probably don't want a head shot on the card, but have uploaded just in case. Please use Adobe Illustrator.
Probably just the logo. Something that is clean, possible a repeated design such as the logo. Would like to consider UV spotting on back. Try searching for "business cards spot uv" on Google, then look at the "images" link.
SiteAdmin SiteAdmin
Dear Designers, Kindly follow the below mention instructions by the Project holder for better and improve designs: We want to use spot UV on our cards, front and back. Here is a video Link from the printing company we are using. If you are unfamiliar with creating file for Spot UV, it requires one file for the card and a second mask file for the UV spotting. https://www.clipvault.example/watch?v=Qx7rLm2PzA1 Use your creativity, but a couple ideas for the back would be to repeat our logo over and over across the entire back. It may be nice to somehow put our website within those repeated logos. Or it may not be nice, depending on how it looks. You could also just make our logo with URL on the back. For the front, you will have to be creative to make it work. Our logo could be UV spotted. And then probably some sort of nice design that covers a portion of the front, keeping in mind that the uv spot coating design can overlap anything. Or maybe it would look best to only spot uv our logo. The content for the card is in our creative brief. We would also like to include "We Love Referrals!" somewhere on the card. Here are a few images for some ideas. Keep in mind that we don't want a copy of what is done with these ideas. They are simply ideas of what can be done with UV spotting. https://pressglow.example/assets/images/gallery/business-cards/images/a1b2c3d4e5f60718293a4b5c6d7e8f90.png https://pressglow.example/assets/uploads/spot_uv_marlow_business_cards.jpg http://media.shopweave.example/51730264/Renata-Pell-spot-gloss-silver-foil-spot-uv-silk-unique-cool-business-cards_full.jpeg http://www.quartzlinecards.example/images/img-gallery/silk-business-card-with-spot-uv-harrow-cellars.jpg http://i01.i.tradepix.example/wsphoto/v2/813406572_2/Custom-Spot-UV-business-card-matt-coated-paper-350gsm-High-quality.jpg http://www.newswire.example/64028195-silk-laminated-business-cards-with-spot-uv.jpg http://www.atelier-cartes-nord.example/wp-content/uploads/2010/10/carte-commerciale-vernis-selectif.jpg https://pressglow.example/assets/uploads/spot_uv_cards_dravetek.jpg http://www.calloutmailers.example/wp/wp-content/uploads/2013/03/zebra-orange-spot-uv-business-card1.png http://layoutharbor.example/wp-content/uploads/2013/04/square-business-card-29.jpg
fernloft47 fernloft47
I forgot to add on that last comment, that the black designs are way to dark for our tastes. Blue on the back looks nice. We prefer the lighter designs on the front of the card.
We are looking for double sided cards with rounded corners and some UV spotting on both sides. We like the design of #96 on the back side, however it looks like there may be some silver foil on the logo. We won't be doing foil, just spotting. There are a lot of nice designs so far, but we need to have the combination of rounded corners and UV spotting. Thanks.

```html
<!DOCTYPE html>
<html lang="en">
<head>
<meta charset="utf-8">
<title>Fern Loft Properties – Business Card</title>
<link rel="stylesheet" href="https://fonts.googleapis.com/css2?family=Montserrat:wght@500;700;800&family=Roboto:wght@400;500&display=swap">
<style>
  :root {
    --stage: #8a8d90;
    --blue-deep: #12327e;
    --blue: #1f4ea8;
    --blue-light: #2f63c2;
    --white: #ffffff;
    --grey-arc: #b9bcc2;
    --ink: #1c2a5c;
  }
  * { box-sizing: border-box; margin: 0; padding: 0; }
  html, body {
    width: 1200px; height: 908px; overflow: hidden;
    background: var(--stage);
  }
  .stage {
    position: relative; width: 1200px; height: 908px;
    display: flex; align-items: center; justify-content: center; gap: 60px;
  }
  .card {
    position: relative; width: 520px; height: 297px;
    border-radius: 24px; overflow: hidden;
    box-shadow: 0 10px 24px rgba(0,0,0,.28);
  }
  /* Back side */
  .card-back {
    background: linear-gradient(135deg, var(--blue-light), var(--blue-deep));
  }
  .back-pattern {
    position: absolute; inset: 0;
    background: linear-gradient(160deg, rgba(255,255,255,.10), rgba(255,255,255,0) 60%);
  }
  .wordmark {
    font-family: "Montserrat", sans-serif; font-weight: 800;
    letter-spacing: .02em; line-height: 1;
  }
  .back-logo {
    position: absolute; left: 44px; bottom: 62px;
    display: flex; align-items: center; gap: 12px;
    color: var(--white); font-size: 34px;
  }
  .back-logo .mark {
    width: 30px; height: 30px; border-radius: 4px; background: var(--white);
  }
  .back-logo small {
    display: block; font-size: 11px; letter-spacing: .42em; margin-top: 6px; text-align: right;
  }
  /* Front side */
  .card-front { background: var(--blue); }
  .front-shapes { position: absolute; inset: 0; }
  .front-logo {
    position: absolute; left: 46px; top: 118px;
    display: flex; align-items: center; gap: 12px;
    color: var(--blue-deep); font-size: 30px;
  }
  .front-logo .mark {
    width: 28px; height: 28px; border-radius: 4px; background: var(--blue-deep);
  }
  .front-logo small {
    display: block; font-size: 10px; letter-spacing: .42em; margin-top: 6px; text-align: right;
  }
  .person {
    position: absolute; right: 28px; top: 26px; text-align: right;
    color: var(--white); font-family: "Roboto", sans-serif;
  }
  .person .name { font-size: 20px; font-weight: 500; }
  .person .title { font-size: 12px; margin-top: 3px; opacity: .92; }
  .contacts {
    position: absolute; right: 28px; bottom: 24px;
    list-style: none; text-align: right;
    color: var(--white); font-family: "Roboto", sans-serif; font-size: 10.5px; line-height: 1.55;
  }
  .contacts li { display: flex; justify-content: flex-end; align-items: center; gap: 6px; }
  .contacts .group { margin-top: 6px; }
  .contacts svg { width: 10px; height: 10px; flex: none; }
</style>
</head>
<body>
<main class="stage">
  <section class="card card-back" aria-label="Card back">
    <div class="back-pattern" role="img" aria-label="Repeated brand pattern in tonal blue spot gloss"></div>
    <div class="back-logo">
      <span class="mark"></span>
      <span class="wordmark">FERN LOFT<small>PROPERTIES</small></span>
    </div>
  </section>

  <section class="card card-front" aria-label="Card front">
    <svg class="front-shapes" viewBox="0 0 520 297" preserveAspectRatio="none">
      <path d="M0 0 H270 C360 60 330 240 300 297 H0 Z" fill="var(--grey-arc)"/>
      <path d="M0 0 H250 C340 60 312 240 282 297 H0 Z" fill="var(--white)"/>
    </svg>
    <div class="front-logo">
      <span class="mark"></span>
      <span class="wordmark">FERN LOFT<small>PROPERTIES</small></span>
    </div>
    <div class="person">
      <p class="name">Anselm Varga</p>
      <p class="title">Managing Broker</p>
    </div>
    <ul class="contacts">
      <li>Licensed in ID &amp; MT</li>
      <li class="group">4382 SW Route 14, Ste 305
        <svg viewBox="0 0 10 10"><path d="M5 0.5a3 3 0 0 1 3 3c0 2.3-3 6-3 6s-3-3.7-3-6a3 3 0 0 1 3-3z" fill="#fff"/></svg></li>
      <li>Ashbury, ID 83701</li>
      <li class="group">208-555-0147 Direct
        <svg viewBox="0 0 10 10"><path d="M2 0.8l2 2-1 1.2c.6 1.2 1.6 2.2 2.8 2.8l1.2-1 2 2-1.2 1.4C4.8 9 1 5.2.6 2z" fill="#fff"/></svg></li>
      <li>208-555-0193 Cell
        <svg viewBox="0 0 10 10"><rect x="2.5" y=".5" width="5" height="9" rx="1" fill="#fff"/></svg></li>
      <li class="group">anselm@fernloftpm.example
        <svg viewBox="0 0 10 10"><rect x=".5" y="2" width="9" height="6" rx="1" fill="#fff"/><path d="M.8 2.4L5 5.6l4.2-3.2" stroke="var(--blue)" fill="none"/></svg></li>
      <li>www.fernlofthomes.example
        <svg viewBox="0 0 10 10"><circle cx="5" cy="5" r="4.2" fill="none" stroke="#fff"/><path d="M.8 5h8.4M5 .8c-2 2.5-2 5.9 0 8.4M5 .8c2 2.5 2 5.9 0 8.4" stroke="#fff" fill="none" stroke-width=".8"/></svg></li>
    </ul>
  </section>
</main>
</body>
</html>
```